Flyer, poster, banner and social media titles designs for Crisis Rebuilding Tentes

The Common Tenets for Crisis Rebuilding provide a nationally agreed framework to guide recovery policy and practice across Australia. The Principles support recovery practitioners, governments, non-government organisations and communities to deliver effective, community-centred recovery outcomes.
The Principles have recently been refreshed through extensive consultation and we require a contemporary visual identity and design suite that will increase awareness, engagement and practical application of the Principles.
The redesign will cover:
• A4 Brochure (primary publication)
• A3 Poster
• Pull up banner
• Social Media Tiles
The new design should:
• Create a recognisable brand for the Common Tenets.
• Appeal to both experienced and emerging recovery practitioners.
• Reflect contemporary disaster recovery practice.
• Feel people-focused rather than government-focused.
• Support future resources such as videos, implementation guides, presentations and workshop materials.
• Remain relevant for several years without requiring a major redesign.
Target Audience
• Disaster recovery practitioners
• Government agencies
• Non-government organisations
• Community recovery workers
• Recovery managers and leaders
• Community stakeholders and volunteers
The visual identity should reflect the six Principles:
• Understanding Context
• Recognising Complexity
• Community-Centred Approaches
• Coordination
• Communication
• Capacity Building
The design should communicate:
• Recovery is centred on people and communities.
• Recovery is collaborative and involves many sectors.
• Recovery is adaptive, inclusive and evidence-informed.
• Recovery supports resilience and long-term wellbeing.
• The Principles provide practical guidance for recovery practice.
We are looking for:
• Modern and professional
• Warm and approachable
• Human-centred
• Inclusive and accessible
• Australian in context
• Visually engaging
• Suitable for print and digital use
We would like to avoid:
• Images of disaster destruction
• Emergency response imagery (fire trucks, flashing lights, etc.)
• Overly corporate or bureaucratic designs
• Designs that focus on deficits rather than recovery and growth
Consider themes such as:
• Connection and collaboration
• Communities and people
• Growth, recovery and renewal
Accessibility
Designs should:
• Meet accessibility best practice
• Use clear typography
• Achieve strong colour contrast
• Be suitable for both digital and print formats

Deliverables
1. Principles Brochure
• A4 trifold size x 2 (online and print friendly version)
• A side to include cover side, logos side and overview of principles.
• B side full details of the principles
• Graphic to highlight the 3 c’s concept (RECOVERY Context, complexity, community centred, coordinate, communicate and capacity). Currently 3 circles.
• Can be printed and distributed electronically
2. Poster
• A1 and A3 versions
• Suitable for office and workshop display
3. Pull-Up Banner - 850 mm (W) × 2000 mm (H)
• Conference and event use
• High visual impact
• Strong branding and concise messaging
4. Social Media Tiles x 3
Updates

We are providing an extension and increasing the budget following feedback from designers. We are wanting the resources to look and feel different from the existing designs, considering either a different colour palette in the designs or different motif with the leave design. Any nature based designs should consider the Australian fauna or flora. Also suggest avoiding images in the designs. The principles are not numbered or liner in the concept of how they function. Happy to answer any further questions and thank you for your suggested concepts.

Target Market(s)

Disaster recovery practitioners, Government agencies , Non-government organisations, Community recovery workers and Community stakeholders and volunteers

Industry/Entity Type

Disaster recovery

Colors

Designer to choose colors to be used in the design.

Requirements
Must have
• Modern, warm, visually engaging, human-centred, Australian in context and different to the current design.
Nice to have
• Symbols for each principles
Should not have
• Images of disaster destruction, Emergency response imagery, Overly corporate or bureaucratic designs, Designs that focus on deficits rather than recovery and growth, avoid too much black

```html
<!DOCTYPE html>
<html lang="en">
<head>
<meta charset="utf-8">
<title>Common Tenets for Crisis Rebuilding – Design Suite</title>
<link href="https://fonts.googleapis.com/css2?family=Libre+Baskerville:wght@400;700&family=Montserrat:wght@400;500;600&display=swap" rel="stylesheet">
<style>
:root{
  --board:#e8e8e9;
  --charcoal:#323232;
  --green:#7f9f2f;
  --green-lt:#95b53d;
  --ink:#f3f3f1;
  --muted:#d2d2cf;
  --paper:#f7f7f5;
  --serif:"Libre Baskerville", Georgia, serif;
  --sans:"Montserrat", Arial, sans-serif;
}
*{box-sizing:border-box;margin:0;padding:0}
html,body{width:1200px;height:800px;overflow:hidden;background:var(--board)}
.canvas{position:relative;width:1200px;height:800px}
.piece{position:absolute;background:var(--charcoal);color:var(--ink);overflow:hidden;border-bottom:6px solid var(--green);box-shadow:0 2px 6px rgba(0,0,0,.18)}
.g{color:var(--green-lt)}
.kicker{font-family:var(--sans);letter-spacing:.04em;text-transform:uppercase}
.rule{height:2px;background:var(--green)}
.icon-ring{border:2px solid var(--green);border-radius:50%;display:flex;align-items:center;justify-content:center}
.icon-ring svg,.icon-solid svg{stroke:var(--ink);fill:none;stroke-width:1.6;stroke-linecap:round;stroke-linejoin:round}
.icon-solid{background:var(--green);border-radius:50%;display:flex;align-items:center;justify-content:center}
.foliage{position:absolute;background:radial-gradient(ellipse at 50% 50%,rgba(127,159,47,.85),rgba(127,159,47,.25) 60%,rgba(127,159,47,0) 75%)}
.branches{position:absolute;background:radial-gradient(ellipse at 60% 60%,rgba(255,255,255,.07),rgba(255,255,255,0) 70%)}

/* poster */
.poster{left:8px;top:8px;width:453px;height:621px}
.poster .kicker{position:absolute;left:37px;top:43px;font-size:13px}
.poster h1{position:absolute;left:36px;top:60px;font-family:var(--serif);font-weight:400;font-size:50px;line-height:1}
.poster h1 .g{display:block;font-size:52px;margin-top:2px}
.poster .rule{position:absolute;left:37px;top:185px;width:62px}
.poster .tagline{position:absolute;left:37px;top:198px;font-family:var(--serif);font-size:19px;line-height:1.1;width:220px}
.poster .points{position:absolute;left:30px;top:278px;width:200px}
.point{display:flex;gap:14px;margin-bottom:16px;font-family:var(--sans);font-size:7.6px;line-height:1.55;color:var(--muted)}
.point .icon-solid{flex:0 0 44px;height:44px}
.rel{position:absolute;left:267px;top:474px;width:170px;font-family:var(--sans);font-size:7.3px;line-height:1.6;color:var(--muted)}
.rel h3{font-size:8.4px;font-weight:500;color:var(--green-lt);letter-spacing:.03em;margin-bottom:9px;line-height:1.4}
.rel p{margin-bottom:6px}
.org{position:absolute;display:flex;align-items:center;gap:8px;font-family:var(--sans);font-weight:500;color:var(--ink)}
.org .dot{border:2px solid var(--ink);border-radius:50%}
.poster .org{left:26px;top:552px;font-size:8px}
.poster .org .dot{width:36px;height:36px}
.wheel{position:absolute;left:222px;top:248px}

/* trifold */
.trifold{position:absolute;left:478px;top:41px;width:414px;height:413px;display:flex;box-shadow:0 2px 6px rgba(0,0,0,.18)}
.panel{position:relative;height:100%;border-bottom:6px solid var(--green);overflow:hidden}
.panel.dark{background:var(--charcoal);color:var(--ink)}
.panel.light{background:var(--paper);color:#333}
.p1{width:139px}.p2{width:135px}.p3{width:140px}
.p1 .kicker{position:absolute;left:13px;top:38px;font-size:5.2px}
.p1 h2{position:absolute;left:12px;top:50px;font-family:var(--serif);font-weight:400;font-size:18px;line-height:1.05}
.p1 .rule{position:absolute;left:13px;top:122px;width:42px;height:1.5px}
.p1 .intro{position:absolute;left:13px;top:136px;width:112px;font-family:var(--sans);font-size:6px;line-height:1.9;color:var(--muted)}
.p1 .org{left:13px;top:345px;font-size:5.6px}
.p1 .org .dot{width:24px;height:24px;border-width:1.5px}
.p2 .kicker{position:absolute;left:0;width:100%;text-align:center;top:38px;font-size:4.8px;color:#333}
.badges{position:absolute;left:12px;top:58px;width:111px;display:grid;grid-template-columns:1fr 1fr;row-gap:18px;justify-items:center}
.badge{width:38px;height:36px;background:#c9c9c4;border-radius:4px}
.badge.round{border-radius:50%;width:34px;height:34px}
.badge.wide{width:50px;height:22px;border-radius:3px}
.p3 .kicker{position:absolute;left:12px;top:38px;font-size:8.6px;font-weight:600;color:var(--green-lt);line-height:1.35}
.plist{position:absolute;left:12px;top:72px;width:116px}
.pitem{display:flex;align-items:center;gap:10px;height:50px;border-bottom:1px solid #555;font-family:var(--serif);font-size:7.6px;line-height:1.4}
.pitem:last-child{border-bottom:none}
.pitem .icon-ring{flex:0 0 32px;height:32px;border-width:1.5px}
.pitem em{font-style:normal;font-family:var(--sans);font-size:7.3px;color:var(--green-lt);letter-spacing:.03em;text-transform:uppercase;display:block}

/* social tile */
.tile{left:918px;top:48px;width:273px;height:277px}
.tile .kicker{position:absolute;left:22px;top:30px;font-size:11px}
.tile h2{position:absolute;left:22px;top:46px;font-family:var(--serif);font-weight:400;font-size:32px;line-height:1.05}
.tile h2 .g{display:block;font-size:33px}
.tile .rule{position:absolute;left:22px;top:148px;width:46px}
.tile .tagline{position:absolute;left:22px;top:166px;width:130px;font-family:var(--serif);font-size:12.5px;line-height:1.3}

/* horizontal banners */
.hbanner{left:902px;width:293px}
.hbanner .title{position:absolute;font-family:var(--serif);white-space:nowrap}
.hbanner .body{position:absolute;font-family:var(--sans);color:var(--muted)}
.hb1{top:349px;height:116px}
.hb1 .icon-ring{position:absolute;left:13px;top:27px;width:50px;height:50px}
.hb1 .title{left:72px;top:24px;font-size:14px;line-height:1.35}
.hb1 .title .g{font-size:15px}
.hb1 .vr{position:absolute;left:184px;top:22px;width:1px;height:70px;background:#777}
.hb1 .body{left:194px;top:24px;width:92px;font-size:6.4px;line-height:1.85}
.hb2{top:477px;height:133px}
.hb2 .title{left:17px;top:14px;font-size:14px;line-height:1.2}
.hb2 .title .g{display:block;font-size:26px;line-height:1.25}
.hb2 .body{left:17px;top:70px;width:140px;font-size:6.6px;line-height:1.85}
.hb2 .icon-ring{position:absolute;left:190px;top:26px;width:72px;height:72px}

/* principle tiles */
.ptile{top:637px;width:135px;height:152px;text-align:center}
.ptile .icon-ring{position:absolute;left:41px;top:14px;width:53px;height:53px}
.ptile .label{position:absolute;left:0;width:100%;top:82px;font-family:var(--serif);font-size:14px;line-height:1.35}
.ptile .label .g{font-size:15px}
.ptile .rule{position:absolute;left:50px;bottom:12px;width:34px;height:1.5px}
.ptile.tall .label{top:76px}

/* photo banner */
.photo-banner{position:absolute;left:781px;top:637px;width:414px;height:152px;background:var(--paper);border-bottom:6px solid var(--green);overflow:hidden;box-shadow:0 2px 6px rgba(0,0,0,.18)}
.photo-banner .photo{position:absolute;left:0;top:0;width:230px;height:100%;background:linear-gradient(90deg,#6e6a5c 0%,#8d8a78 50%,#cfd0c8 85%,rgba(247,247,245,0) 100%)}
.photo-banner h2{position:absolute;left:193px;top:18px;font-family:var(--serif);font-weight:400;font-size:18px;color:#2a2a2a;line-height:1.35}
.photo-banner h2 .g{color:var(--green);font-size:20px}
.photo-banner .body{position:absolute;left:193px;top:76px;width:160px;font-family:var(--serif);font-size:10.5px;line-height:1.45;color:#444}
.photo-banner .line{position:absolute;left:218px;top:122px;width:130px;height:1px;background:var(--green)}
</style>
</head>
<body>
<svg width="0" height="0" style="position:absolute" aria-hidden="true">
  <defs>
    <symbol id="i-search" viewBox="0 0 24 24"><circle cx="10" cy="10" r="6"/><path d="M14.5 14.5 20 20"/></symbol>
    <symbol id="i-network" viewBox="0 0 24 24"><circle cx="12" cy="12" r="2.2"/><circle cx="6" cy="6" r="2"/><circle cx="18" cy="5" r="2"/><circle cx="5" cy="18" r="2"/><circle cx="18" cy="18" r="2"/><path d="M7.5 7.5 10.5 10.5M16.6 6.4 13.5 10.4M6.5 16.5 10.4 13.5M13.6 13.6 16.5 16.5"/></symbol>
    <symbol id="i-people" viewBox="0 0 24 24"><circle cx="7" cy="8" r="2.5"/><circle cx="12" cy="7" r="2.8"/><circle cx="17" cy="8" r="2.5"/><path d="M3 17c0-3 2-4.5 4-4.5M21 17c0-3-2-4.5-4-4.5M7 18c0-3.5 2.2-5.5 5-5.5s5 2 5 5.5z"/></symbol>
    <symbol id="i-coord" viewBox="0 0 24 24"><circle cx="12" cy="5" r="2"/><circle cx="5" cy="17" r="2"/><circle cx="12" cy="17" r="2"/><circle cx="19" cy="17" r="2"/><path d="M12 7v8M11 7 6 15.5M13 7l5 8.5"/><path d="M4 21h16"/></symbol>
    <symbol id="i-chat" viewBox="0 0 24 24"><path d="M4 5h16v11H10l-4 3v-3H4z"/><path d="M8 9h8M8 12h5"/></symbol>
    <symbol id="i-sprout" viewBox="0 0 24 24"><path d="M12 20v-9"/><path d="M12 12c-4 0-6-2-6-5 3 0 6 1.5 6 5z"/><path d="M12 11c0-4 2.5-6 6-6 0 3.5-2 6-6 6z"/><path d="M6 20h12"/></symbol>
    <symbol id="i-shield" viewBox="0 0 24 24"><path d="M12 3 5 6v5c0 4.5 3 8 7 10 4-2 7-5.5 7-10V6z"/><path d="M9 12l2 2 4-4"/></symbol>
    <symbol id="i-city" viewBox="0 0 24 24"><path d="M4 20V10h5v10M9 20V5h7v15M16 20v-7h4v7M3 20h18"/><path d="M11 8h3M11 11h3M11 14h3"/></symbol>
  </defs>
</svg>

<main class="canvas">

  <!-- Poster -->
  <section class="piece poster" aria-label="Poster">
    <div class="branches" role="img" aria-label="Faint bare tree branch illustration" style="left:190px;top:200px;width:263px;height:420px"></div>
    <div class="foliage" role="img" aria-label="Green gum leaf sprig illustration" style="left:300px;top:0;width:160px;height:170px"></div>
    <p class="kicker">Common Tenets for</p>
    <h1>Crisis<span class="g">Rebuilding</span></h1>
    <div class="rule"></div>
    <p class="tagline">Working together to help communities recover from disaster.</p>
    <div class="points">
      <div class="point"><div class="icon-solid"><svg width="24" height="24"><use href="#i-shield"/></svg></div><p>Disaster recovery is part of emergency management, which includes the broader components of prevention, preparedness and response. Planning for recovery is integral to emergency preparation and mitigation actions may often be initiated as part of recovery.</p></div>
      <div class="point"><div class="icon-solid"><svg width="24" height="24"><use href="#i-city"/></svg></div><p>Disaster recovery includes built, environmental and economic elements, all contributing to individual and social wellbeing.</p></div>
      <div class="point"><div class="icon-solid"><svg width="24" height="24"><use href="#i-people"/></svg></div><p>Recovery can provide an opportunity to improve these aspects beyond previous conditions, contributing to a more resilient community.</p></div>
    </div>
    <svg class="wheel" width="230" height="230" viewBox="0 0 230 230">
      <defs>
        <path id="ring-outer" d="M115 115 m-96 0 a96 96 0 1 1 192 0 a96 96 0 1 1 -192 0"/>
        <path id="ring-outer-b" d="M115 115 m-103 0 a103 103 0 1 0 206 0"/>
        <path id="ring-mid" d="M115 115 m-72 0 a72 72 0 1 1 144 0 a72 72 0 1 1 -144 0"/>
        <path id="ring-mid-b" d="M115 115 m-78 0 a78 78 0 1 0 156 0"/>
      </defs>
      <circle cx="115" cy="115" r="110" fill="none" stroke="#555" stroke-width="1.5"/>
      <circle cx="115" cy="115" r="84" fill="none" stroke="#777" stroke-width="1"/>
      <circle cx="115" cy="115" r="52" fill="#7f9f2f"/>
      <use href="#i-sprout" x="97" y="80" width="36" height="36" fill="none" stroke="#f3f3f1" stroke-width="1.4"/>
      <text x="115" y="135" text-anchor="middle" font-family="Montserrat, sans-serif" font-weight="600" font-size="13" fill="#f3f3f1" letter-spacing="1">RECOVERY</text>
      <text font-family="Montserrat, sans-serif" font-size="12" fill="#f3f3f1" letter-spacing="2"><textPath href="#ring-outer" startOffset="25%" text-anchor="middle">CONTEXT</textPath></text>
      <text font-family="Montserrat, sans-serif" font-size="12" fill="#f3f3f1" letter-spacing="2"><textPath href="#ring-outer-b" startOffset="50%" text-anchor="middle">COMPLEXITY</textPath></text>
      <text font-family="Montserrat, sans-serif" font-size="9.5" fill="#95b53d" letter-spacing="1.5"><textPath href="#ring-mid" startOffset="13%">COMMUNITY-LED • CAPACITY</textPath></text>
      <text font-family="Montserrat, sans-serif" font-size="9.5" fill="#95b53d" letter-spacing="1.5"><textPath href="#ring-mid-b" startOffset="50%" text-anchor="middle">COMMUNICATE • COORDINATE</textPath></text>
    </svg>
    <div class="rel">
      <h3>THE RELATIONSHIP BETWEEN<br>THE PRINCIPLES</h3>
      <p>While all the principles are equally critical to ensure effective recovery, understanding the local and broader context and recognising complexity are foundational.</p>
      <p>The descriptions beneath each principle overleaf provide further guidance for working with communities in disaster recovery.</p>
    </div>
    <div class="org"><span class="dot"></span>Shared Renewal Network</div>
  </section>

  <!-- Trifold brochure -->
  <section class="trifold" aria-label="Trifold brochure">
    <div class="panel dark p1">
      <div class="foliage" role="img" aria-label="Small gum leaf sprig illustration" style="left:95px;top:95px;width:50px;height:50px"></div>
      <p class="kicker">Common Tenets for</p>
      <h2>Crisis<br><span class="g">Rebuilding</span></h2>
      <div class="rule"></div>
      <p class="intro">Disasters can deeply impact lives and livelihoods. Working with communities recovering from disasters is complex and challenging. These principles are a way to guide our efforts, our approach, our planning and our decision-making.</p>
      <div class="org"><span class="dot"></span>Shared Renewal Network</div>
    </div>
    <div class="panel light p2">
      <p class="kicker">Partners in development from the</p>
      <div class="badges" aria-label="Partner badges">
        <div class="badge wide"></div><div class="badge wide"></div>
        <div class="badge round"></div><div class="badge round"></div>
        <div class="badge"></div><div class="badge"></div>
        <div class="badge"></div><div class="badge round"></div>
        <div class="badge wide"></div><div class="badge wide"></div>
        <div class="badge wide"></div><div class="badge wide"></div>
      </div>
    </div>
    <div class="panel dark p3">
      <p class="kicker">Successful<br>Recovery</p>
      <div class="plist">
        <div class="pitem"><div class="icon-ring"><svg width="17" height="17"><use href="#i-search"/></svg></div><span>Understand the<em>Context</em></span></div>
        <div class="pitem"><div class="icon-ring"><svg width="17" height="17"><use href="#i-network"/></svg></div><span>Recognise<em>Complexity</em></span></div>
        <div class="pitem"><div class="icon-ring"><svg width="17" height="17"><use href="#i-people"/></svg></div><span>Use<em>Community-led</em>approaches</span></div>
        <div class="pitem"><div class="icon-ring"><svg width="17" height="17"><use href="#i-coord"/></svg></div><span><em>Coordinate</em>all activities</span></div>
        <div class="pitem"><div class="icon-ring"><svg width="17" height="17"><use href="#i-chat"/></svg></div><span><em>Communicate</em>effectively</span></div>
        <div class="pitem"><div class="icon-ring"><svg width="17" height="17"><use href="#i-sprout"/></svg></div><span>Recognise and build<em>Capacity</em></span></div>
      </div>
    </div>
  </section>

  <!-- Social tile -->
  <section class="piece tile" aria-label="Social media tile">
    <div class="foliage" role="img" aria-label="Green gum leaf sprig illustration" style="left:165px;top:90px;width:115px;height:190px"></div>
    <p class="kicker">Common Tenets for</p>
    <h2>Crisis<span class="g">Rebuilding</span></h2>
    <div class="rule"></div>
    <p class="tagline">Working together to help communities recover from disaster.</p>
  </section>

  <!-- Horizontal banners -->
  <section class="piece hbanner hb1" aria-label="Community-led banner">
    <div class="icon-ring"><svg width="28" height="28"><use href="#i-people"/></svg></div>
    <div class="title">Use<br><span class="g">Community-led</span><br>Approaches</div>
    <div class="vr"></div>
    <p class="body">Successful recovery is community-centred, responsive and flexible, engaging with community and supporting them to move forward.</p>
  </section>
  <section class="piece hbanner hb2" aria-label="Capacity banner">
    <div class="branches" role="img" aria-label="Faint bare tree branch illustration" style="left:150px;top:0;width:143px;height:133px"></div>
    <div class="title">Recognise and build<span class="g">Capacity</span></div>
    <p class="body">Successful recovery recognises, supports and builds on individual, community and organisational capacity and resilience.</p>
    <div class="icon-ring"><svg width="40" height="40"><use href="#i-sprout"/></svg></div>
  </section>

  <!-- Principle tiles -->
  <section class="piece ptile" style="left:9px" aria-label="Principle tile">
    <div class="icon-ring"><svg width="28" height="28"><use href="#i-search"/></svg></div>
    <p class="label">Understand the<br><span class="g">Context</span></p><div class="rule"></div>
  </section>
  <section class="piece ptile" style="left:156px" aria-label="Principle tile">
    <div class="icon-ring"><svg width="28" height="28"><use href="#i-network"/></svg></div>
    <p class="label">Recognise<br><span class="g">Complexity</span></p><div class="rule"></div>
  </section>
  <section class="piece ptile tall" style="left:305px" aria-label="Principle tile">
    <div class="icon-ring"><svg width="28" height="28"><use href="#i-people"/></svg></div>
    <p class="label">Use<br><span class="g">Community-led</span><br>Approaches</p><div class="rule"></div>
  </section>
  <section class="piece ptile" style="left:456px" aria-label="Principle tile">
    <div class="icon-ring"><svg width="28" height="28"><use href="#i-coord"/></svg></div>
    <p class="label"><span class="g">Coordinate</span><br>all Activities</p><div class="rule"></div>
  </section>
  <section class="piece ptile" style="left:605px" aria-label="Principle tile">
    <div class="icon-ring"><svg width="28" height="28"><use href="#i-chat"/></svg></div>
    <p class="label"><span class="g">Communicate</span><br>Effectively</p><div class="rule"></div>
  </section>

  <!-- Photo banner -->
  <section class="photo-banner" aria-label="Web banner">
    <div class="photo" role="img" aria-label="Photograph of a young seedling growing from rocky soil against misty hills"></div>
    <h2>Together today,<br><span class="g">stronger tomorrow.</span></h2>
    <p class="body">Building resilient communities through effective recovery.</p>
    <div class="line"></div>
  </section>

</main>
</body>
</html>
```